App UI design needed! For a Password Management Tool

Need a design of a Windows desktop application which is a Password Management Tool, similar to Vaultkin, Brimlock or Keywell, with Business/Enterprise functionalities. Here attached are a few sample pages of Brimlock, and some sample pages of our app called Tessaly. We certainly want to redesign our app.
We need: 1. The layout of the web: top banner, menu, main pane; 2. Form style, main form and sub forms; 3. List style; 4 Fonts and buttons; 5. Logo.
The design should look professional, can attract business customers as well as individual users, and present a strong sense of “Security”. The look and feel should differentiate from well-known products like Vaultkin, Brimlock, Keywell, etc.

```html
<!DOCTYPE html>
<html lang="en">
<head>
<meta charset="utf-8">
<title>Tessaly – Password Manager Screens</title>
<link href="https://fonts.googleapis.com/css2?family=Roboto:wght@400;500;700&display=swap" rel="stylesheet">
<style>
:root{
  --page:#ffffff;
  --side:#2a2d32;
  --top:#1d1f23;
  --main:#25272b;
  --field:#1c1e22;
  --row-hi:#1f2125;
  --line:#3a3d42;
  --text:#ffffff;
  --muted:#b4b7bc;
  --blue:#0d8df2;
  --orange:#f5871f;
}
*{box-sizing:border-box;margin:0;padding:0}
html,body{width:671px;height:1200px;overflow:hidden;background:var(--page);font-family:'Roboto',sans-serif;color:var(--text)}
.screen{position:absolute;left:53px;width:565px;background:var(--main);overflow:hidden}
.s1{top:63px;height:321px}
.s2{top:416px;height:397px}
.s3{top:848px;height:289px}
.sidebar{position:absolute;left:0;top:0;width:132px;height:100%;background:var(--side)}
.brand{position:absolute;left:17px;top:0;height:35px;display:flex;align-items:center;gap:5px;font-size:12px;font-weight:500;color:var(--blue)}
.brand-dot{width:10px;height:10px;border-radius:50%;background:var(--blue)}
.brand-rule{position:absolute;left:0;top:35px;width:132px;height:1px;background:#303339}
.menu{position:absolute;left:0;top:50px;width:132px;list-style:none}
.menu li{height:23.7px;display:flex;align-items:center;font-size:7.5px;font-weight:500;padding-left:17px;position:relative}
.menu li svg{width:7px;height:7px;margin-right:9.5px;fill:#fff}
.menu li.active{background:var(--blue);margin-left:4px;padding-left:13px;border-radius:4px 0 0 4px}
.topbar{position:absolute;left:132px;top:0;right:0;height:35px;background:var(--top)}
.fav{position:absolute;left:39px;top:0;height:35px;display:flex;align-items:center;gap:4px;font-size:7.5px;font-weight:500}
.fav svg{width:7px;height:7px;fill:var(--blue)}
.search{position:absolute;left:173px;top:9px;width:116px;height:17px;border-radius:9px;background:#17191c;font-size:6px;color:#ddd;display:flex;align-items:center;padding-left:9px}
.search svg{position:absolute;right:7px;top:5px;width:7px;height:7px}
.ticon{position:absolute;top:10px;width:15px;height:15px;border-radius:50%;background:#2c2f35;display:flex;align-items:center;justify-content:center}
.ticon svg{width:7px;height:7px;fill:var(--blue)}
.avatar{position:absolute;left:356px;top:8px;width:18px;height:18px;border-radius:50%;background:linear-gradient(#d9dde2,#7c8794)}
.user{position:absolute;left:379px;top:0;height:35px;display:flex;align-items:center;gap:3px;font-size:7px;font-weight:500}
.content{position:absolute;left:132px;top:35px;right:0;bottom:0}
.h1{position:absolute;left:39px;font-size:13px;font-weight:500}
.btn-outline{position:absolute;left:317px;width:80px;height:21px;border:1px solid var(--blue);border-radius:11px;color:var(--blue);font-size:7.5px;font-weight:500;display:flex;align-items:center;justify-content:center}
.col-head{position:absolute;top:59px;font-size:9px;font-weight:500;display:flex;align-items:center;gap:4px}
.list{position:absolute;left:39px;top:81px;width:357px;border-top:1px solid var(--line)}
.row{height:44.3px;border-bottom:1px solid var(--line);position:relative;display:flex;align-items:center}
.row.hi{background:var(--row-hi)}
.site-tile{position:absolute;left:13px;top:9px;width:26px;height:26px;border-radius:3px;background:#fff}
.site-name{position:absolute;left:51px;top:11px;font-size:8.5px;font-weight:500}
.site-mail{position:absolute;left:51px;top:24px;font-size:6.5px;color:var(--muted)}
.used{position:absolute;left:188px;top:18px;font-size:6.5px;color:var(--muted)}
.act{position:absolute;top:16px;width:10px;height:10px}
.tile-lg{position:absolute;left:197px;top:27px;width:39px;height:35px;border-radius:3px;background:#fff}
.field{position:absolute;left:43px;width:347px;height:35px;background:var(--field);border-radius:2px}
.field .lbl{position:absolute;left:12px;top:7px;font-size:7px;color:var(--muted);font-weight:500}
.field .val{position:absolute;left:11px;top:17px;font-size:9.5px;font-weight:500}
.field .eye{position:absolute;right:12px;top:10px;width:16px;height:14px}
.note{position:absolute;left:43px;font-size:7.5px;color:var(--muted);font-weight:500}
.h2{position:absolute;left:43px;top:154px;font-size:13px;font-weight:500}
.strength{position:absolute;left:43px;top:258px;font-size:7.5px;color:var(--orange);font-weight:500;display:flex;align-items:center;gap:3px}
.gen{position:absolute;right:43px;top:258px;font-size:7.5px;color:var(--blue);font-weight:500}
.table{position:absolute;left:39px;top:68px;width:357px;border-collapse:collapse;font-size:7px}
.table th{height:24px;background:var(--field);text-align:left;font-size:8px;font-weight:500}
.table td{height:25px;color:#e8e9eb;border-bottom:1px solid #2b2e33}
.table th:first-child,.table td:first-child{padding-left:8px}
.entries{position:absolute;left:39px;top:212px;font-size:7.5px;font-weight:500}
.pager{position:absolute;top:211px;height:16px;border:1px solid #3a3d42;border-radius:2px;display:flex;align-items:center;justify-content:center;font-size:7.5px;color:var(--blue)}
.pager.plain{border:none}
.pager.sel{color:#fff;border-color:#3a3d42;gap:4px}
.pager.next{border-color:var(--blue)}
</style>
</head>
<body>

<!-- Screen 1: Web Logins list -->
<section class="screen s1">
  <aside class="sidebar">
    <div class="brand"><span class="brand-dot"></span>Tessaly</div>
    <div class="brand-rule"></div>
    <ul class="menu">
      <li><svg viewBox="0 0 10 10"><rect x="0" y="0" width="4.5" height="4.5"/><rect x="5.5" y="0" width="4.5" height="4.5"/><rect x="0" y="5.5" width="4.5" height="4.5"/><rect x="5.5" y="5.5" width="4.5" height="4.5"/></svg>Dashboard</li>
      <li><svg viewBox="0 0 10 10"><circle cx="5" cy="3" r="2.5"/><path d="M1 10c0-3 2-4.5 4-4.5s4 1.5 4 4.5z"/></svg>Users</li>
      <li><svg viewBox="0 0 10 10"><circle cx="3" cy="3" r="2"/><circle cx="7" cy="3" r="2"/><path d="M0 9c0-2.5 1.5-4 3-4s3 1.5 3 4zM4 9c0-2.5 1.5-4 3-4s3 1.5 3 4z"/></svg>Teams</li>
      <li><svg viewBox="0 0 10 10"><path d="M2 0v5a3 3 0 0 0 6 0V2h-1.5v3a1.5 1.5 0 0 1-3 0V0z"/></svg>Client Containers</li>
      <li class="active"><svg viewBox="0 0 10 10"><path d="M3 4V3a2 2 0 0 1 4 0v1h1v6H2V4zm1 0h2V3a1 1 0 0 0-2 0z"/></svg>Web Logins</li>
      <li><svg viewBox="0 0 10 10"><path d="M1 0h5l3 3v7H1z"/></svg>Reports</li>
      <li><svg viewBox="0 0 10 10"><path d="M0 0h5l5 5-5 5-5-5z"/></svg>My Tags</li>
      <li><svg viewBox="0 0 10 10"><circle cx="5" cy="5" r="5"/></svg>Personal</li>
      <li><svg viewBox="0 0 10 10"><circle cx="5" cy="5" r="4"/></svg>Setting</li>
    </ul>
  </aside>
  <header class="topbar">
    <div class="fav"><svg viewBox="0 0 10 10"><path d="M5 0l1.5 3.3 3.5.4-2.6 2.4.7 3.5L5 7.8 1.9 9.6l.7-3.5L0 3.7l3.5-.4z"/></svg>Favourites</div>
    <div class="search">Search...<svg viewBox="0 0 10 10" fill="none" stroke="#0d8df2" stroke-width="1.6"><circle cx="4" cy="4" r="3"/><path d="M6.2 6.2L9.5 9.5"/></svg></div>
    <div class="ticon" style="left:308px"><svg viewBox="0 0 10 10"><circle cx="5" cy="5" r="4"/></svg></div>
    <div class="ticon" style="left:326px"><svg viewBox="0 0 10 10"><path d="M5 0a3 3 0 0 1 3 3v3l1.5 2h-9L2 6V3a3 3 0 0 1 3-3zM4 9h2a1 1 0 0 1-2 0z"/></svg></div>
    <div class="avatar" role="img" aria-label="User profile photo"></div>
    <div class="user">John Doe <svg width="6" height="6" viewBox="0 0 10 10" fill="none" stroke="#fff" stroke-width="1.5"><path d="M2 3.5l3 3 3-3"/></svg></div>
  </header>
  <main class="content">
    <h1 class="h1" style="top:23px">Web Logins</h1>
    <div class="btn-outline" style="top:22px">Add Password</div>
    <div class="col-head" style="left:39px">Title</div>
    <div class="col-head" style="left:227px">Last Used <svg width="7" height="7" viewBox="0 0 10 10" fill="none" stroke="#fff" stroke-width="1.5"><path d="M2 3.5l3 3 3-3"/></svg></div>
    <div class="list">
      <div class="row hi">
        <div class="site-tile"></div>
        <div class="site-name">forgehub.io</div>
        <div class="site-mail">lmoreno@mailpost.net</div>
        <div class="used">2 hours ago</div>
        <svg class="act" style="left:306px" viewBox="0 0 10 10"><rect width="10" height="10" rx="1.5" fill="#fff"/><path d="M3 7l4-4M4 3h3v3" stroke="#1f2125" stroke-width="1.4" fill="none"/></svg>
        <svg class="act" style="left:331px" viewBox="0 0 10 10" fill="#fff"><circle cx="1.5" cy="5" r="1.2"/><circle cx="5" cy="5" r="1.2"/><circle cx="8.5" cy="5" r="1.2"/></svg>
      </div>
      <div class="row"><div class="site-tile"></div><div class="site-name">forgehub.io</div><div class="site-mail">lmoreno@mailpost.net</div><div class="used">2 hours ago</div></div>
      <div class="row"><div class="site-tile"></div><div class="site-name">forgehub.io</div><div class="site-mail">lmoreno@mailpost.net</div><div class="used">2 hours ago</div></div>
      <div class="row" style="border-bottom:none"><div class="site-tile"></div><div class="site-name">forgehub.io</div><div class="site-mail">lmoreno@mailpost.net</div><div class="used">2 hours ago</div></div>
    </div>
  </main>
</section>

<!-- Screen 2: Login detail form -->
<section class="screen s2">
  <aside class="sidebar">
    <div class="brand"><span class="brand-dot"></span>Tessaly</div>
    <div class="brand-rule"></div>
    <ul class="menu">
      <li><svg viewBox="0 0 10 10"><rect x="0" y="0" width="4.5" height="4.5"/><rect x="5.5" y="0" width="4.5" height="4.5"/><rect x="0" y="5.5" width="4.5" height="4.5"/><rect x="5.5" y="5.5" width="4.5" height="4.5"/></svg>Dashboard</li>
      <li><svg viewBox="0 0 10 10"><circle cx="5" cy="3" r="2.5"/><path d="M1 10c0-3 2-4.5 4-4.5s4 1.5 4 4.5z"/></svg>Users</li>
      <li><svg viewBox="0 0 10 10"><circle cx="3" cy="3" r="2"/><circle cx="7" cy="3" r="2"/><path d="M0 9c0-2.5 1.5-4 3-4s3 1.5 3 4zM4 9c0-2.5 1.5-4 3-4s3 1.5 3 4z"/></svg>Teams</li>
      <li><svg viewBox="0 0 10 10"><path d="M2 0v5a3 3 0 0 0 6 0V2h-1.5v3a1.5 1.5 0 0 1-3 0V0z"/></svg>Client Containers</li>
      <li class="active"><svg viewBox="0 0 10 10"><path d="M3 4V3a2 2 0 0 1 4 0v1h1v6H2V4zm1 0h2V3a1 1 0 0 0-2 0z"/></svg>Web Logins</li>
      <li><svg viewBox="0 0 10 10"><path d="M1 0h5l3 3v7H1z"/></svg>Reports</li>
      <li><svg viewBox="0 0 10 10"><path d="M0 0h5l5 5-5 5-5-5z"/></svg>My Tags</li>
      <li><svg viewBox="0 0 10 10"><circle cx="5" cy="5" r="5"/></svg>Personal</li>
      <li><svg viewBox="0 0 10 10"><circle cx="5" cy="5" r="4"/></svg>Setting</li>
    </ul>
  </aside>
  <header class="topbar">
    <div class="fav"><svg viewBox="0 0 10 10"><path d="M5 0l1.5 3.3 3.5.4-2.6 2.4.7 3.5L5 7.8 1.9 9.6l.7-3.5L0 3.7l3.5-.4z"/></svg>Favourites</div>
    <div class="search">Search...<svg viewBox="0 0 10 10" fill="none" stroke="#0d8df2" stroke-width="1.6"><circle cx="4" cy="4" r="3"/><path d="M6.2 6.2L9.5 9.5"/></svg></div>
    <div class="ticon" style="left:308px"><svg viewBox="0 0 10 10"><circle cx="5" cy="5" r="4"/></svg></div>
    <div class="ticon" style="left:326px"><svg viewBox="0 0 10 10"><path d="M5 0a3 3 0 0 1 3 3v3l1.5 2h-9L2 6V3a3 3 0 0 1 3-3zM4 9h2a1 1 0 0 1-2 0z"/></svg></div>
    <div class="avatar" role="img" aria-label="User profile photo"></div>
    <div class="user">John Doe <svg width="6" height="6" viewBox="0 0 10 10" fill="none" stroke="#fff" stroke-width="1.5"><path d="M2 3.5l3 3 3-3"/></svg></div>
  </header>
  <main class="content">
    <div class="tile-lg"></div>
    <div class="field" style="top:79px"><span class="lbl">Title*</span><span class="val">forgehub.io</span></div>
    <div class="note" style="top:119px">*Required</div>
    <h2 class="h2">Login Details</h2>
    <div class="field" style="top:173px"><span class="lbl">Email Or User Name</span><span class="val">lmoreno@mailpost.net</span></div>
    <div class="field" style="top:219px"><span class="lbl">Password</span><span class="val" style="letter-spacing:-0.5px">•••••••••••••••••</span>
      <svg class="eye" viewBox="0 0 16 14" fill="none" stroke="#fff" stroke-width="1.6"><path d="M1 7c2-3 4.5-4.5 7-4.5S13 4 15 7c-2 3-4.5 4.5-7 4.5S3 10 1 7z"/><circle cx="8" cy="7" r="2.2"/><path d="M12 1L4 13"/></svg>
    </div>
    <div class="strength"><svg width="8" height="8" viewBox="0 0 10 10"><path d="M5 0l5 9.5H0z" fill="#f5871f"/><path d="M5 3.5v3M5 7.5v1" stroke="#25272b" stroke-width="1.2"/></svg>Moderate Password</div>
    <div class="gen">Generate Password</div>
    <div class="field" style="top:283px"><span class="lbl">Website Address*</span><span class="val">https://forgehub.io/login</span></div>
    <div class="note" style="top:322px">*Required</div>
  </main>
</section>

<!-- Screen 3: Client Containers table -->
<section class="screen s3">
  <aside class="sidebar">
    <div class="brand"><span class="brand-dot"></span>Tessaly</div>
    <div class="brand-rule"></div>
    <ul class="menu">
      <li><svg viewBox="0 0 10 10"><rect x="0" y="0" width="4.5" height="4.5"/><rect x="5.5" y="0" width="4.5" height="4.5"/><rect x="0" y="5.5" width="4.5" height="4.5"/><rect x="5.5" y="5.5" width="4.5" height="4.5"/></svg>Dashboard</li>
      <li><svg viewBox="0 0 10 10"><circle cx="5" cy="3" r="2.5"/><path d="M1 10c0-3 2-4.5 4-4.5s4 1.5 4 4.5z"/></svg>Users</li>
      <li><svg viewBox="0 0 10 10"><circle cx="3" cy="3" r="2"/><circle cx="7" cy="3" r="2"/><path d="M0 9c0-2.5 1.5-4 3-4s3 1.5 3 4zM4 9c0-2.5 1.5-4 3-4s3 1.5 3 4z"/></svg>Teams</li>
      <li><svg viewBox="0 0 10 10"><path d="M2 0v5a3 3 0 0 0 6 0V2h-1.5v3a1.5 1.5 0 0 1-3 0V0z"/></svg>Client Containers</li>
      <li class="active"><svg viewBox="0 0 10 10"><path d="M3 4V3a2 2 0 0 1 4 0v1h1v6H2V4zm1 0h2V3a1 1 0 0 0-2 0z"/></svg>Web Logins</li>
      <li><svg viewBox="0 0 10 10"><path d="M1 0h5l3 3v7H1z"/></svg>Reports</li>
      <li><svg viewBox="0 0 10 10"><path d="M0 0h5l5 5-5 5-5-5z"/></svg>My Tags</li>
      <li><svg viewBox="0 0 10 10"><circle cx="5" cy="5" r="5"/></svg>Personal</li>
      <li><svg viewBox="0 0 10 10"><circle cx="5" cy="5" r="4"/></svg>Setting</li>
    </ul>
  </aside>
  <header class="topbar">
    <div class="fav"><svg viewBox="0 0 10 10"><path d="M5 0l1.5 3.3 3.5.4-2.6 2.4.7 3.5L5 7.8 1.9 9.6l.7-3.5L0 3.7l3.5-.4z"/></svg>Favourites</div>
    <div class="search">Search...<svg viewBox="0 0 10 10" fill="none" stroke="#0d8df2" stroke-width="1.6"><circle cx="4" cy="4" r="3"/><path d="M6.2 6.2L9.5 9.5"/></svg></div>
    <div class="ticon" style="left:308px"><svg viewBox="0 0 10 10"><circle cx="5" cy="5" r="4"/></svg></div>
    <div class="ticon" style="left:326px"><svg viewBox="0 0 10 10"><path d="M5 0a3 3 0 0 1 3 3v3l1.5 2h-9L2 6V3a3 3 0 0 1 3-3zM4 9h2a1 1 0 0 1-2 0z"/></svg></div>
    <div class="avatar" role="img" aria-label="User profile photo"></div>
    <div class="user">John Doe <svg width="6" height="6" viewBox="0 0 10 10" fill="none" stroke="#fff" stroke-width="1.5"><path d="M2 3.5l3 3 3-3"/></svg></div>
  </header>
  <main class="content">
    <h1 class="h1" style="top:24px">Client Containers</h1>
    <div class="btn-outline" style="top:22px">Add Password</div>
    <table class="table">
      <thead><tr><th style="width:128px">Client Containers Des</th><th style="width:86px">Ip</th><th style="width:75px">Remark</th><th>Status</th></tr></thead>
      <tbody>
        <tr><td>Corvex-Node-East-2.....</td><td>203.0.113.124</td><td>Client-1</td><td>Active</td></tr>
        <tr><td>Corvex-Node-East-2.....</td><td>203.0.113.124</td><td>Client-1</td><td>Active</td></tr>
        <tr><td>Corvex-Node-East-2.....</td><td>203.0.113.124</td><td>Client-1</td><td>Active</td></tr>
        <tr><td>Corvex-Node-East-2.....</td><td>203.0.113.124</td><td>Client-1</td><td>Active</td></tr>
      </tbody>
    </table>
    <div class="entries">Showing 1 to 4 of 14 entries</div>
    <div class="pager sel" style="left:280px;width:23px">6 <svg width="6" height="6" viewBox="0 0 10 10" fill="none" stroke="#fff" stroke-width="1.6"><path d="M2 3.5l3 3 3-3"/></svg></div>
    <div class="pager" style="left:312px;width:15px;color:#fff">‹</div>
    <div class="pager" style="left:329px;width:15px">1</div>
    <div class="pager plain" style="left:346px;width:15px">2</div>
    <div class="pager plain" style="left:363px;width:15px">3</div>
    <div class="pager next" style="left:381px;width:15px">›</div>
  </main>
</section>

</body>
</html>
```